Webdesign
Zielgruppe
Briefing für die neue Website von TELORI GmbH
Allgemeine Informationen:
Name des Unternehmens: TELORI GmbH
Branche: Maschinenbau
Zweck der Website: Eine Unternehmenswebsite, die informiert, was die Firma macht und es potenziellen Kunden oder Partnern ermöglicht, in Kontakt zu treten.
Zielgruppe:
Hauptzielgruppe: Anlagenbauer, Maschinenbauer, Anlagenbetreiber aus verschiedenen Branchen.
Design-Anforderungen: Die Zielgruppe erwartet Professionalität und Klarheit, also sollte die Website eine hohe Qualität, Professionalität und Benutzerfreundlichkeit reflektieren.
Design-Vorlieben:
Farbschema & Stil: Das Design sollte sich an den bereitgestellten Logos orientieren. Der gewünschte Stil ist modern und klar.
Inspirationsquellen: Die Logos des Unternehmens, die dem Briefing beigefügt werden.
Inhalt und Struktur:
Einseitiges Design: Die Website sollte nur eine Seite zum Herunterscrollen haben.
Unternehmensvorstellung: Ein kurzer Abschnitt, der beschreibt, wer TELORI GmbH ist und was das Unternehmen macht.
Leistungsübersicht: Eine klare Darstellung der Dienstleistungen oder Produkte, die TELORI GmbH anbietet. Dies kann durch Symbole, kurze Texte oder Bilder dargestellt werden.
Kontaktmöglichkeit: Ein Kontaktformular oder zumindest klare Kontaktinformationen (Telefon, E-Mail, Adresse), so dass Besucher leicht in Kontakt treten können.
Aufgabenstellung
siehe oben

```html
<!DOCTYPE html>
<html lang="de">
<head>
<meta charset="utf-8">
<title>TELORI GmbH – Maschinenbau</title>
<link rel="stylesheet" href="https://fonts.googleapis.com/css2?family=Montserrat:wght@400;500;600;700&display=swap">
<style>
:root{
  --red:#c0161c;
  --red-dark:#a50f14;
  --ink:#1e1e1e;
  --text:#333;
  --grey-bg:#efefef;
  --dark:#2b2b2b;
  --yellow:#f7c52b;
  --white:#fff;
}
*{box-sizing:border-box;margin:0;padding:0}
html,body{width:1200px;height:3458px;overflow:hidden;background:var(--white)}
body{font-family:"Montserrat",sans-serif;color:var(--text);position:relative}
.page{position:relative;width:1200px;height:3458px;overflow:hidden}
.abs{position:absolute}

/* Navigation */
.nav{left:0;top:0;width:1200px;height:54px;background:var(--white);z-index:5}
.brand{left:148px;top:0;height:54px;display:flex;align-items:center;gap:8px;font-weight:700;font-size:24px;color:var(--red);letter-spacing:1px}
.brand-dot{width:14px;height:14px;border-radius:50%;background:var(--red)}
.nav-links{right:140px;top:0;height:54px;display:flex}
.nav-links a{display:flex;align-items:center;padding:0 18px;font-size:13px;font-weight:500;color:var(--ink);text-decoration:none}
.nav-links a.active{background:var(--red);color:var(--white);font-weight:600}

/* Hero */
.hero{left:0;top:54px;width:1200px;height:530px;background:radial-gradient(ellipse at 70% 40%,#4a3b30 0%,#2a211b 45%,#15110e 100%)}
.hero-photo{position:absolute;inset:0;background:linear-gradient(90deg,rgba(120,70,30,.35),rgba(40,30,25,.1) 50%,rgba(150,90,40,.3))}
.hero h1{left:146px;top:122px;width:460px;font-size:37px;line-height:43px;font-weight:600;color:var(--white)}
.hero .lead{left:149px;top:221px;font-size:16px;color:var(--white)}
.btn-call{left:150px;top:275px;width:228px;height:48px;background:var(--red);color:var(--white);display:flex;align-items:center;justify-content:center;gap:12px;font-size:19px;font-weight:600}
.dots{display:flex;gap:7px}
.dots span{width:8px;height:8px;border-radius:50%;background:var(--red)}
.dots span.on{background:var(--white)}
.hero .dots{left:566px;top:420px}
.wave{position:absolute;left:0;width:1200px}

/* Wer wir sind */
.section-title{width:1200px;text-align:center;font-size:27px;font-weight:600;color:var(--red)}
.about-text{left:280px;top:720px;width:640px;text-align:center;font-size:13px;line-height:19px;color:var(--ink)}

/* Was wir tun */
.services{left:0;top:880px;width:1200px;height:990px;background:linear-gradient(180deg,#2d2d2d,#3a3a3a 50%,#242424)}
.services-title{color:var(--white)}
.card{width:275px;height:366px;background:var(--white);box-shadow:0 2px 6px rgba(0,0,0,.3)}
.card-head{height:44px;background:var(--red);color:var(--white);font-size:15px;font-weight:600;display:flex;align-items:center;justify-content:center}
.card-img{height:157px}
.card p{padding:16px 20px 0;font-size:11.5px;line-height:15.5px;color:var(--ink)}
.card .btn{display:block;margin:12px auto 0;width:104px;height:28px;background:var(--red);color:var(--white);font-size:12px;font-weight:600;text-align:center;line-height:28px}
.img-a{background:linear-gradient(135deg,#5b6a78,#c9d3dc 40%,#3d5c88)}
.img-b{background:linear-gradient(135deg,#0f3b5c,#2d6a8c 50%,#d4a62c)}
.img-c{background:linear-gradient(135deg,#bfc6cc,#6e7a84 50%,#e5e9ec)}
.img-d{background:linear-gradient(135deg,#2f8fb0,#5bb8d4 50%,#1f5f78)}
.img-e{background:linear-gradient(135deg,#8c8a85,#c66a2a 40%,#9aa3ab)}

/* Stärken */
.strengths{left:0;top:1850px;width:1200px;height:620px;background:var(--grey-bg)}
.strength{width:282px;height:190px;background:var(--white);box-shadow:0 1px 4px rgba(0,0,0,.12)}
.badge{position:absolute;left:10px;top:0;width:66px;height:100px}
.strength h3{position:absolute;left:92px;top:22px;width:180px;font-size:15px;font-weight:500;color:var(--red);line-height:18px}
.strength p{position:absolute;left:94px;top:58px;width:176px;font-size:11.5px;line-height:16px;color:var(--ink)}

/* Testimonials */
.quote-mark{font-size:110px;line-height:1;color:#c7c7c7;font-family:"Georgia",serif;font-weight:700}
.testimonial{font-size:12.5px;line-height:19px;color:var(--ink)}
.author{font-size:12.5px;font-weight:600;color:var(--red)}
.t-dots span{background:#c7c7c7}
.t-dots span.on{background:var(--red)}

/* Kontakt */
.contact{left:0;top:2872px;width:1200px;height:503px;background:linear-gradient(180deg,#c9252a,#b81a1f)}
.contact .section-title{color:var(--white)}
.field{height:36px;background:var(--white);font-size:12px;color:#555;padding:0 12px;display:flex;align-items:center}
.field.area{align-items:flex-start;padding-top:12px;height:106px}
.send{left:518px;top:3185px;width:168px;height:36px;background:var(--yellow);color:var(--ink);font-weight:600;font-size:15px;display:flex;align-items:center;justify-content:center}
.info{display:flex;align-items:flex-start;gap:14px;color:var(--white)}
.info .txt{font-size:16px}

/* Footer */
.footer{left:0;top:3375px;width:1200px;height:83px;background:var(--dark)}
.footer-brand{left:152px;top:0;height:83px;display:flex;align-items:center;gap:8px;font-weight:700;font-size:22px;color:#6a6a6a;letter-spacing:1px}
.social{left:535px;top:36px;display:flex;gap:17px}
.social span{width:10px;height:10px;border-radius:50%;background:#555}
.copy{right:150px;top:33px;font-size:12px;color:#8a8a8a}
</style>
</head>
<body>
<div class="page">

  <!-- Hero -->
  <section class="abs hero">
    <div class="hero-photo" role="img" aria-label="Foto: Ingenieur mit Schutzhelm von hinten in einer beleuchteten Industriehalle"></div>
  </section>
  <h1 class="abs hero" style="background:none;height:auto;left:146px;top:176px;width:460px;font-size:37px;line-height:43px;font-weight:600;color:#fff">Lorem ipsum dolor sit amet, consectetur</h1>
  <p class="abs" style="left:149px;top:275px;font-size:16px;color:#fff">Lorem ipsum dolor sit amet, consectetur</p>
  <div class="abs btn-call" style="top:329px">
    <svg width="20" height="20" viewBox="0 0 24 24" fill="none" stroke="#fff" stroke-width="1.8"><path d="M5 3h4l2 5-2.5 1.5a11 11 0 0 0 6 6L16 13l5 2v4a2 2 0 0 1-2 2A17 17 0 0 1 3 5a2 2 0 0 1 2-2z"/></svg>
    <span>1800.555.019</span>
  </div>
  <div class="abs dots" style="left:566px;top:474px"><span class="on"></span><span></span><span></span><span></span><span></span></div>
  <svg class="wave" style="top:480px" height="120" viewBox="0 0 1200 120" preserveAspectRatio="none">
    <path d="M0 40 C250 110 450 110 700 70 C900 40 1050 45 1200 75 L1200 120 L0 120Z" fill="#fff"/>
    <path d="M0 30 C250 105 450 108 700 70 C900 40 1050 45 1200 75 L1200 85 C1050 58 900 55 700 84 C450 120 250 118 0 45Z" fill="#c0161c"/>
  </svg>

  <!-- Navigation -->
  <header class="abs nav">
    <div class="abs brand"><span class="brand-dot"></span>TELORI</div>
    <nav class="abs nav-links">
      <a class="active" href="#">Startseite</a>
      <a href="#">Wer wir sind</a>
      <a href="#">Was wir tun</a>
      <a href="#">Kontakt</a>
    </nav>
  </header>

  <!-- Wer wir sind -->
  <h2 class="abs section-title" style="top:672px">Wer wir sind</h2>
  <p class="abs about-text">TELORI ist ein führendes Unternehmen im Bereich moderner Maschinenbau. Wir sind spezialisiert auf die Konzeption, Konstruktion und Herstellung maßgeschneiderter Maschinen und Anlagen, die den höchsten Ansprüchen der heutigen Industrie gerecht werden.</p>

  <!-- Was wir tun -->
  <section class="abs services" role="img" aria-label="Hintergrundfoto: abgedunkelte Fertigungshalle"></section>
  <svg class="wave" style="top:870px" height="70" viewBox="0 0 1200 70" preserveAspectRatio="none">
    <path d="M0 0 L1200 0 L1200 35 C1000 0 800 10 550 45 C300 70 150 40 0 10Z" fill="#fff"/>
    <path d="M550 45 C800 10 1000 0 1200 35 L1200 55 C1000 18 800 28 550 55 C400 70 300 60 260 55 C350 58 450 55 550 45Z" fill="#c0161c"/>
  </svg>
  <h2 class="abs section-title services-title" style="top:950px">Was wir tun</h2>

  <div class="abs card" style="left:150px;top:1006px"><div class="card-head">Quis ipsum suspendisse</div><div class="card-img img-a" role="img" aria-label="Foto: CNC-Maschinen mit blauen Kabeln"></div><p>Lorem ipsum dolor sit amet, consectetur adipiscing elit, sed do eiusmod tempor incididunt ut labore et dolore magna aliqua. Quis ipsum suspendisse ultrices gravida. Risus commodo viverra maecenas accumsan</p><span class="btn">Kontakt</span></div>
  <div class="abs card" style="left:462px;top:1006px"><div class="card-head">Quis ipsum suspendisse</div><div class="card-img img-b" role="img" aria-label="Foto: gelber Industrieroboter mit digitalen Symbolen"></div><p>Lorem ipsum dolor sit amet, consectetur adipiscing elit, sed do eiusmod tempor incididunt ut labore et dolore magna aliqua. Quis ipsum suspendisse ultrices gravida. Risus commodo viverra maecenas accumsan</p><span class="btn">Kontakt</span></div>
  <div class="abs card" style="left:774px;top:1006px"><div class="card-head">Quis ipsum suspendisse</div><div class="card-img img-c" role="img" aria-label="Foto: Produktionsanlage aus Edelstahl"></div><p>Lorem ipsum dolor sit amet, consectetur adipiscing elit, sed do eiusmod tempor incididunt ut labore et dolore magna aliqua. Quis ipsum suspendisse ultrices gravida. Risus commodo viverra maecenas accumsan</p><span class="btn">Kontakt</span></div>
  <div class="abs card" style="left:150px;top:1404px"><div class="card-head">Quis ipsum suspendisse</div><div class="card-img img-d" role="img" aria-label="Foto: blaue Elektromotoren in einer Reihe"></div><p>Lorem ipsum dolor sit amet, consectetur adipiscing elit, sed do eiusmod tempor incididunt ut labore et dolore magna aliqua. Quis ipsum suspendisse ultrices gravida. Risus commodo viverra maecenas accumsan</p><span class="btn">Kontakt</span></div>
  <div class="abs card" style="left:462px;top:1404px"><div class="card-head">Quis ipsum suspendisse</div><div class="card-img img-e" role="img" aria-label="Foto: Roboterarme in einer Fertigungsstraße"></div><p>Lorem ipsum dolor sit amet, consectetur adipiscing elit, sed do eiusmod tempor incididunt ut labore et dolore magna aliqua. Quis ipsum suspendisse ultrices gravida. Risus commodo viverra maecenas accumsan</p><span class="btn">Kontakt</span></div>
  <div class="abs card" style="left:774px;top:1404px"><div class="card-head">Quis ipsum suspendisse</div><div class="card-img img-a" role="img" aria-label="Foto: CNC-Bearbeitungszentrum"></div><p>Lorem ipsum dolor sit amet, consectetur adipiscing elit, sed do eiusmod tempor incididunt ut labore et dolore magna aliqua. Quis ipsum suspendisse ultrices gravida. Risus commodo viverra maecenas accumsan</p><span class="btn">Kontakt</span></div>

  <!-- Unsere Stärken -->
  <section class="abs strengths"></section>
  <svg class="wave" style="top:1820px" height="70" viewBox="0 0 1200 70" preserveAspectRatio="none">
    <path d="M0 0 L1200 0 L1200 40 C1000 15 800 12 550 30 C300 50 150 40 0 20Z" fill="#262626"/>
    <path d="M0 20 C150 40 300 50 550 30 C800 12 1000 15 1200 40 L1200 70 L0 70Z" fill="#efefef"/>
    <path d="M0 20 C150 40 300 50 550 30 C600 26 640 24 680 22 C620 30 580 36 550 38 C300 58 150 48 0 32Z" fill="#c0161c"/>
  </svg>
  <h2 class="abs section-title" style="top:1914px">Unsere Stärken</h2>

  <div class="abs strength" style="left:150px;top:1973px">
    <svg class="badge" viewBox="0 0 66 100"><path d="M0 0H66V67A33 33 0 0 1 0 67Z" fill="#c0161c"/><circle cx="33" cy="52" r="14" fill="none" stroke="#fff" stroke-width="2"/></svg>
    <h3>INNOVATION</h3>
    <p>Wir setzen modernste CAD/CAM-Software und CNC-Technologien ein, um Präzision und Effizienz in der Produktion sicherzustellen.</p>
  </div>
  <div class="abs strength" style="left:459px;top:1973px">
    <svg class="badge" viewBox="0 0 66 100"><path d="M0 0H66V67A33 33 0 0 1 0 67Z" fill="#c0161c"/><circle cx="33" cy="50" r="14" fill="none" stroke="#fff" stroke-width="2"/></svg>
    <h3>QUALITÄT</h3>
    <p>Unsere hochqualifizierten Ingenieure und Techniker arbeiten mit Leidenschaft daran, innovative Lösungen zu entwickeln und höchste Qualitätsstandards zu erfüllen.</p>
  </div>
  <div class="abs strength" style="left:766px;top:1973px">
    <svg class="badge" viewBox="0 0 66 100"><path d="M0 0H66V67A33 33 0 0 1 0 67Z" fill="#c0161c"/><circle cx="33" cy="50" r="16" fill="none" stroke="#fff" stroke-width="2"/><path d="M36 38 28 52h8l-4 12" fill="none" stroke="#fff" stroke-width="2"/></svg>
    <h3>NACHHALTIGKEIT</h3>
    <p>Umweltfreundlichkeit und Nachhaltigkeit sind integraler Bestandteil unserer Philosophie. Wir integrieren diese Prinzipien in all unsere Produkte und Produktionsprozesse.</p>
  </div>
  <div class="abs strength" style="left:302px;top:2193px">
    <svg class="badge" viewBox="0 0 66 100"><path d="M0 0H66V67A33 33 0 0 1 0 67Z" fill="#c0161c"/><path d="M14 62c8 0 12-6 22-4l12 2" fill="none" stroke="#fff" stroke-width="2"/></svg>
    <h3>KUNDENZUFRIE-<br>DENHEIT</h3>
    <p style="top:58px">Bei TELORI steht die Zufriedenheit unserer Kunden an erster Stelle. Wir arbeiten eng mit Ihnen zusammen, um Ihre individuellen Anforderungen zu verstehen und zu erfüllen.</p>
  </div>
  <div class="abs strength" style="left:609px;top:2193px">
    <svg class="badge" viewBox="0 0 66 100"><path d="M0 0H66V67A33 33 0 0 1 0 67Z" fill="#c0161c"/><circle cx="38" cy="52" r="14" fill="none" stroke="#fff" stroke-width="2"/><path d="M38 44v8l5 4M12 46h12M14 54h10M16 62h8" fill="none" stroke="#fff" stroke-width="2"/></svg>
    <h3>SCHNELLIGKEIT</h3>
    <p>Unsere kurzen Lieferzeiten und erstklassiger Kundensupport gewährleisten, dass Sie stets bestens betreut werden.</p>
  </div>

  <!-- Testimonials -->
  <svg class="wave" style="top:2430px" height="60" viewBox="0 0 1200 60" preserveAspectRatio="none">
    <path d="M0 0 L1200 0 L1200 30 C900 15 700 40 450 50 C250 55 100 40 0 25Z" fill="#efefef"/>
    <path d="M0 25 C100 40 250 55 450 50 C700 40 900 15 1200 30 L1200 60 L0 60Z" fill="#fff"/>
    <path d="M0 10 C100 30 250 50 450 45 C550 42 620 38 680 34 C600 44 520 50 450 52 C250 58 100 44 0 22Z" fill="#c0161c"/>
  </svg>
  <div class="abs quote-mark" style="left:146px;top:2510px">“</div>
  <h2 class="abs section-title" style="top:2546px">Was unser Kunde sagt</h2>
  <p class="abs testimonial" style="left:149px;top:2609px;width:405px">Quis ipsum suspendisse ultrices gravida. Risus commodo viverra maecenas accumsan lacus vel facilisis. Risus commodo viverra maecenas accumsan lacus vel facilisis.&nbsp; Lorem ipsum dolor sit amet, consectetur adipiscing elit, sed do eiusmod tempor incididunt ut labore et dolore magna aliqua.</p>
  <p class="abs author" style="left:149px;top:2722px">- Ruben Faltig</p>
  <p class="abs testimonial" style="left:633px;top:2609px;width:420px">Lorem ipsum dolor sit amet, consectetur adipiscing elit, sed do eiusmod tempor incididunt ut labore et dolore magna aliqua. Quis ipsum suspendisse ultrices gravida. Risus commodo viverra maecenas accumsan lacus vel facilisis.</p>
  <p class="abs author" style="left:637px;top:2722px">- Mara Lindquist</p>
  <div class="abs quote-mark" style="left:1002px;top:2712px">”</div>
  <div class="abs dots t-dots" style="left:566px;top:2802px"><span class="on"></span><span></span><span></span><span></span><span></span></div>

  <!-- Kontakt -->
  <section class="abs contact" role="img" aria-label="Hintergrundfoto: Maschinenhalle in Rot getönt"></section>
  <svg class="wave" style="top:2840px" height="60" viewBox="0 0 1200 60" preserveAspectRatio="none">
    <path d="M0 0 L1200 0 L1200 10 C950 25 750 45 500 40 C300 36 150 28 0 14Z" fill="#fff"/>
    <path d="M0 14 C150 28 300 36 500 40 C750 45 950 25 1200 10 L1200 14 C950 32 750 54 500 50 C300 46 150 36 0 20Z" fill="#3a3a3a"/>
  </svg>
  <h2 class="abs section-title" style="top:2934px;font-size:26px">Schneller Kontakt</h2>
  <p class="abs" style="left:0;top:2974px;width:1200px;text-align:center;font-size:12px;color:#fff">Risus commodo viverra maecenas accumsan lacus vel facilisis.</p>
  <div class="abs field" style="left:333px;top:3013px;width:172px">Name</div>
  <div class="abs field" style="left:518px;top:3013px;width:168px">Email</div>
  <div class="abs field" style="left:699px;top:3013px;width:168px">Telefon</div>
  <div class="abs field area" style="left:333px;top:3062px;width:534px">Wie können wir Ihnen helfen?</div>
  <div class="abs send">SENDEN</div>

  <div class="abs info" style="left:234px;top:3278px">
    <svg width="20" height="24" viewBox="0 0 20 24"><path d="M10 0a9 9 0 0 0-9 9c0 7 9 15 9 15s9-8 9-15a9 9 0 0 0-9-9z" fill="#fff"/><circle cx="10" cy="9" r="3.5" fill="#c0161c"/></svg>
    <div class="txt" style="font-size:13px;line-height:18px">xxxxxxxxxxxxxxxxxxxxxxxxx<br>xxxxxxxxxxxxxxxxxxxxxxxxx<br>xxxxxxxxxxxxxxxxxxxx</div>
  </div>
  <div class="abs info" style="left:541px;top:3278px">
    <svg width="24" height="18" viewBox="0 0 24 18" fill="none" stroke="#fff" stroke-width="1.6"><rect x="1" y="1" width="22" height="16"/><path d="M1 1l11 9 11-9"/></svg>
    <div class="txt">kontakt@telori.de</div>
  </div>
  <div class="abs info" style="left:797px;top:3278px">
    <svg width="22" height="22" viewBox="0 0 24 24" fill="none" stroke="#fff" stroke-width="1.8"><path d="M5 3h4l2 5-2.5 1.5a11 11 0 0 0 6 6L16 13l5 2v4a2 2 0 0 1-2 2A17 17 0 0 1 3 5a2 2 0 0 1 2-2z"/></svg>
    <div class="txt" style="font-size:18px">1800.555.019</div>
  </div>

  <!-- Footer -->
  <footer class="abs footer">
    <div class="abs footer-brand"><span class="brand-dot" style="background:#6a6a6a"></span>TELORI</div>
    <div class="abs social"><span></span><span></span><span></span><span></span><span></span></div>
    <p class="abs copy">© 2023 telori.de</p>
  </footer>
</div>
</body>
</html>
```